TaviLo Gastronomic Social Network

Tavi Lo is a Gastronomic Social Network that is focused on the relationship between restaurants and customers, creating new channels to communicate with themselves and developing new tools to modernize the classic menus. In Tavi Lo people will see images, videos and texts related on gastronomy shared by the bests restaurants of their cities in real time. Therefore the users will feel how easy is to choose a new restaurant only few minutes before leaving their homes and how useful is to choose a meal with the images of the digital menu in order to have the best experience possible.

Target Market(s)

The direct customers of the company are the restaurants, who pay monthly to post marketing content and their digital menu. The profile of the clients will not be too restrictive: from a restaurant that offers live music and drinks to a classic and expensive restaurant.

The final users of the product are families, couples, professionals and everyone who is interested in discovering new restaurants and good gastronomy.

Requirements
Must have
• We have the idea that after the splash screen show the last registered plates from the restaurants like in snapreel story. On the story we will show the plate for the current time like lunch or dinner, a logo of the restaurant, a small description and the price.
• When selected the plate the user will be redirected to a page will restaurant details showing the selected plate as first item on restaurant menu.
• For each plate we will have a page description showing ingredients, price, harmonization and button to reserve a table.
• Reserve a table is a page for reservation.
• Also we have a page for customer info, last selected plates and restaurants.

```html
<!DOCTYPE html>
<html lang="en">
<head>
<meta charset="utf-8">
<title>Tavi Lo — Splash</title>
<link rel="stylesheet" href="https://fonts.googleapis.com/css2?family=Marcellus&display=swap">
<style>
  :root {
    --plum: #52213d;
    --ink: #ffffff;
    --accent: #f5a400;
  }
  html, body {
    margin: 0;
    padding: 0;
    width: 675px;
    height: 1200px;
    overflow: hidden;
    background: var(--plum);
  }
  .splash {
    position: relative;
    width: 675px;
    height: 1200px;
    background: var(--plum);
  }
  .brand-name {
    position: absolute;
    left: 0;
    right: 0;
    top: 528px;
    margin: 0;
    text-align: center;
    font-family: "Marcellus", serif;
    font-weight: 400;
    font-size: 92px;
    line-height: 1;
    color: var(--ink);
    letter-spacing: 0;
  }
  .loader {
    position: absolute;
    left: 292px;
    top: 880px;
    width: 90px;
    height: 90px;
  }
  .loader circle { fill: var(--ink); }
  .accent-bar {
    position: absolute;
    left: 0;
    bottom: 0;
    width: 675px;
    height: 6px;
    background: var(--accent);
  }
</style>
</head>
<body>
  <main class="splash">
    <h1 class="brand-name">Tavi Lo</h1>

    <svg class="loader" viewBox="0 0 90 90" aria-label="Loading">
      <circle cx="45" cy="5"  r="4" opacity="0.35"/>
      <circle cx="65" cy="10" r="4" opacity="0.25"/>
      <circle cx="80" cy="25" r="4" opacity="0.0"/>
      <circle cx="85" cy="45" r="4" opacity="0.6"/>
      <circle cx="80" cy="65" r="4" opacity="0.6"/>
      <circle cx="65" cy="80" r="4" opacity="0.6"/>
      <circle cx="45" cy="85" r="4" opacity="0.6"/>
      <circle cx="25" cy="80" r="4" opacity="0.6"/>
      <circle cx="10" cy="65" r="4" opacity="0.6"/>
      <circle cx="5"  cy="45" r="4" opacity="0.6"/>
      <circle cx="10" cy="25" r="4" opacity="0.55"/>
      <circle cx="25" cy="10" r="4" opacity="0.45"/>
    </svg>

    <div class="accent-bar"></div>
  </main>
</body>
</html>
```